ZOVA Framework. the way you communicate in every situation and in all environments.

I would like you to create a diagram depicting a very specific process of communication. it must follow the look of the diagram that i have attached. this is going to be used in a book called BEDROCK. it is going to explain the fact that we communicate all the same way using this process as we communicate. it starts with the fact that everyone takes everything that is said personally and then moves on to filters, which is your own agenda or experience kicking in. then you move to your why it matters, which is your motivation and ends with the choice of words you use when you communicate. if you are going to be successful then you must separate the person from the issue.

Target Market(s)

market is executive business people around the world

Industry/Entity Type

Consulting

Font styles to use
Sans Serif

Colors

Designer to choose only greyscale colors for use in the design.

Requirements
Must have
• I would like it to have a diving/ocean/snorkel feel to it. The analogy we are using is to make a deep dive when you are communicating. it must have every part of the diagram you see, it starts at the top with the zova framework (and the words) it then connects to the filters which connects to the why it matters with connects to the words and then end with the separating the person from the issue.
Nice to have
• we are writing a black and white book NO color. therefore the words should be clear and easy to read. Each section should be able to stand on its own so we can write about it separately.
Should not have
• the diagram DOES NOT have to look like the one i gave you. it must explain the fact that it starts with ZOVA and ends with Separate and must pass through the three areas to get to the SEPARATE.

```html
<!DOCTYPE html>
<html lang="en">
<head>
<meta charset="utf-8">
<title>Bedrock – ZOVA Framework</title>
<link rel="stylesheet" href="https://fonts.googleapis.com/css2?family=Oswald:wght@500;700&family=Roboto+Condensed:ital,wght@1,300;1,400&display=swap">
<style>
  :root {
    --ink: #000000;
    --paper: #ffffff;
  }
  * { margin: 0; padding: 0; box-sizing: border-box; }
  html, body { width: 927px; height: 1200px; overflow: hidden; background: var(--paper); }
  .page { position: relative; width: 927px; height: 1200px; background: var(--paper); color: var(--ink); }

  .page-header {
    position: absolute; left: 60px; top: 50px; width: 788px; height: 40px;
    display: flex; align-items: center; gap: 16px;
  }
  .book-title {
    font-family: "Oswald", sans-serif; font-weight: 700; font-size: 32px;
    letter-spacing: 7px; line-height: 1; white-space: nowrap;
  }
  .header-rule { flex: 1; height: 2px; background: var(--ink); }

  .page-footer {
    position: absolute; left: 63px; top: 1122px; width: 777px; height: 34px;
    display: flex; align-items: center; gap: 16px;
  }
  .footer-rule { flex: 1; height: 2px; background: var(--ink); }
  .site-address {
    font-family: "Oswald", sans-serif; font-weight: 500; font-size: 22px;
    letter-spacing: 3.5px; line-height: 34px; white-space: nowrap;
  }

  .diagram { position: absolute; left: 0; top: 0; width: 927px; height: 1200px; }

  .stage {
    position: absolute; width: 160px; height: 170px;
    display: flex; flex-direction: column; align-items: center; justify-content: center;
    text-align: center;
  }
  .stage-title {
    font-family: "Oswald", sans-serif; font-weight: 700; font-size: 22px;
    line-height: 25px; text-transform: uppercase; margin-bottom: 8px;
  }
  .stage-text {
    font-family: "Roboto Condensed", sans-serif; font-style: italic; font-weight: 300;
    font-size: 15.5px; line-height: 19px;
  }
  .stage--zova    { left: 383px; top: 290px; }
  .stage--filters { left: 137px; top: 527px; }
  .stage--why     { left: 383px; top: 527px; }
  .stage--words   { left: 628px; top: 527px; }
  .stage--do      { left: 383px; top: 767px; }
</style>
</head>
<body>
<main class="page">
  <header class="page-header">
    <h1 class="book-title">BEDROCK</h1>
    <span class="header-rule"></span>
  </header>

  <svg class="diagram" viewBox="0 0 927 1200" aria-hidden="true">
    <g class="connectors" fill="none" stroke="var(--ink)" stroke-linecap="round">
      <path d="M430 322 C300 320 205 390 195 560" stroke-width="78"/>
      <path d="M720 660 C730 790 650 850 520 860" stroke-width="78"/>
      <path d="M300 590 L630 590" stroke-width="44"/>
    </g>
    <g class="nodes" fill="var(--paper)" stroke="var(--ink)" stroke-width="13">
      <circle cx="463" cy="373" r="88"/>
      <circle cx="217" cy="612" r="93"/>
      <circle cx="463" cy="612" r="90"/>
      <circle cx="708" cy="612" r="93"/>
      <circle cx="463" cy="852" r="95"/>
    </g>
    <g class="badges">
      <circle cx="463" cy="262" r="28" fill="var(--paper)"/>
      <circle cx="463" cy="262" r="23" fill="var(--ink)"/>
      <g class="icon-share" fill="var(--paper)" stroke="var(--paper)" stroke-width="2.5">
        <line x1="469" y1="253" x2="456" y2="262"/><line x1="456" y1="262" x2="469" y2="271"/>
        <circle cx="469" cy="253" r="4.5"/><circle cx="456" cy="262" r="4.5"/><circle cx="469" cy="271" r="4.5"/>
      </g>

      <circle cx="463" cy="508" r="28" fill="var(--paper)"/>
      <circle cx="463" cy="508" r="23" fill="var(--ink)"/>
      <text x="463" y="518" text-anchor="middle" fill="var(--paper)" font-family="Oswald, sans-serif" font-weight="700" font-size="28">?</text>

      <circle cx="149" cy="537" r="28" fill="var(--paper)"/>
      <circle cx="149" cy="537" r="23" fill="var(--ink)"/>
      <g class="icon-sliders" stroke="var(--paper)" stroke-width="2.5" fill="var(--paper)">
        <line x1="141" y1="525" x2="141" y2="549"/><line x1="149" y1="525" x2="149" y2="549"/><line x1="157" y1="525" x2="157" y2="549"/>
        <rect x="138" y="538" width="6" height="5"/><rect x="146" y="529" width="6" height="5"/><rect x="154" y="535" width="6" height="5"/>
      </g>

      <circle cx="768" cy="537" r="28" fill="var(--paper)"/>
      <circle cx="768" cy="537" r="23" fill="var(--ink)"/>
      <path class="icon-bubble" d="M768 526 c9 0 14 5 14 10 s-6 10 -14 10 c-2 0 -4 0 -5 -1 l-7 4 l2 -6 c-3 -2 -4 -4 -4 -7 c0 -5 5 -10 14 -10z" fill="none" stroke="var(--paper)" stroke-width="3"/>

      <circle cx="463" cy="757" r="28" fill="var(--paper)"/>
      <circle cx="463" cy="757" r="23" fill="var(--ink)"/>
      <path class="icon-tick" d="M451 757 l8 8 l15 -15" fill="none" stroke="var(--paper)" stroke-width="5" stroke-linecap="round" stroke-linejoin="round"/>
    </g>
  </svg>

  <section class="stage stage--zova">
    <h2 class="stage-title">ZOVA<br>Framework</h2>
    <p class="stage-text">When Words Are<br>Taken Personally,<br>What Happens?</p>
  </section>
  <section class="stage stage--filters">
    <h2 class="stage-title">Your<br>Filters</h2>
    <p class="stage-text">An Accumulation<br>Of Your Experience,<br>Knowledge<br>And Values</p>
  </section>
  <section class="stage stage--why">
    <h2 class="stage-title">Why It<br>Matters</h2>
    <p class="stage-text">This Is Your<br>Compass. It Is What<br>Motivates You,<br>What Drives You</p>
  </section>
  <section class="stage stage--words">
    <h2 class="stage-title">Your<br>Words</h2>
    <p class="stage-text">This Is Your<br>Immediate Response,<br>Verbal Or Perhaps<br>Non-verbal</p>
  </section>
  <section class="stage stage--do">
    <h2 class="stage-title">What<br>To Do</h2>
    <p class="stage-text">Separate The<br>Person From The<br>Issue</p>
  </section>

  <footer class="page-footer">
    <span class="footer-rule"></span>
    <span class="site-address">DEEPDIVEPRESS.COM</span>
  </footer>
</main>
</body>
</html>
```